Revamping and duplicating of existing business card

We are a painting and decorating business based in London and need a couple of business cards made up for the following people.

1. Marla Penhallow
2. Toby Renwick

Measurements - 85 X 55 mm
Font: Blue highway
Colour: No idea! Would be great to have a pantone for the pink if possible?

I’ve attached all the logos and old artwork etc.
Here are the amendments I would definitely like...

1. Marla

format mobile number correctly: 07451 386 902

Add title: Decorator
Use: Penhallow Decorating Logo
Add twitter logo & @penhallowdecor
Add tradeverify logo
Add HFG Logo
Make it all look beautiful/revamp/tweak - whatever you think…

2. Toby

Decorator

07623 519 840
toby@penhallowdecorating.co.uk
Updates

Hello! Thanks so much for all your designs. This is such a great way to get these things done... Just to clarify, Please do not alter our logo at all. The 'splat' appears on our van, tshirts, quotes etc and is very much part of our branding. Colour scheme: Pink, black and white. Thanks Marla

Reason: Not 100% sold on any of the designs so far but very grateful for all the submissions. Keep it simple and quirky please. Thanks Marla

Industry/Entity Type

Painting

Requirements
Must have
• Pink & Black Colour scheme
Penhallow Decorating Logo
Blue Highway font

```html
<!DOCTYPE html>
<html lang="en">
<head>
<meta charset="utf-8">
<title>Penhallow Decorating – Business Cards</title>
<link rel="stylesheet" href="https://fonts.googleapis.com/css2?family=Oswald:wght@400;500&display=swap">
<style>
  :root {
    --page-bg: #ececec;
    --card-bg: #ffffff;
    --splat-pink: #d6338f;
    --ink: #111111;
    --logo-ink: #222222;
    --social-blue: #3d8fd1;
    --listing-red: #d7262b;
    --badge-navy: #27307a;
    --card-edge: #cfcfcf;
  }
  * { box-sizing: border-box; margin: 0; padding: 0; }
  html, body {
    width: 992px;
    height: 1200px;
    overflow: hidden;
    background: var(--page-bg);
    font-family: "Oswald", "Arial Narrow", sans-serif;
    color: var(--ink);
  }
  .canvas { position: relative; width: 992px; height: 1200px; }

  .card {
    position: absolute;
    left: 119px;
    width: 766px;
    height: 494px;
    background: var(--card-bg);
    border: 1px solid var(--card-edge);
    overflow: hidden;
  }
  .card--front { top: 67px; }
  .card--back  { top: 626px; }

  .brand-mark {
    position: absolute;
    border-radius: 50%;
    background: var(--splat-pink);
    display: flex;
    align-items: center;
    justify-content: center;
    text-align: center;
  }
  .brand-mark__name {
    font-weight: 400;
    color: var(--logo-ink);
    line-height: 1.05;
  }
  .card--front .brand-mark { left: 215px; top: 80px; width: 360px; height: 360px; }
  .card--front .brand-mark__name { font-size: 28px; padding-left: 30px; }
  .card--back .brand-mark { left: -160px; top: -40px; width: 420px; height: 360px; }
  .card--back .brand-mark__name { font-size: 30px; padding-left: 160px; padding-top: 30px; }

  .front-email {
    position: absolute;
    right: 10px;
    bottom: 22px;
    font-size: 25px;
    font-weight: 500;
    letter-spacing: -0.6px;
  }

  .contact {
    position: absolute;
    right: 30px;
    top: 40px;
    text-align: right;
  }
  .contact__name {
    font-size: 46px;
    font-weight: 500;
    letter-spacing: -1px;
    line-height: 1.1;
  }
  .contact__title { font-size: 24px; font-weight: 500; line-height: 1.1; }
  .contact__phone { font-size: 25px; font-weight: 500; margin-top: 62px; letter-spacing: -0.5px; }
  .contact__email { font-size: 25px; font-weight: 500; margin-top: 14px; letter-spacing: -0.6px; }
  .contact__social {
    display: flex;
    justify-content: flex-end;
    align-items: center;
    gap: 16px;
    margin-top: 14px;
    font-size: 25px;
    font-weight: 500;
    letter-spacing: -0.5px;
  }
  .social-square {
    width: 52px;
    height: 52px;
    background: var(--social-blue);
    border-radius: 3px;
  }

  .listing {
    position: absolute;
    left: 36px;
    bottom: 38px;
    text-align: center;
  }
  .listing__lead { font-size: 12px; font-weight: 400; margin-bottom: 2px; }
  .listing__name {
    font-size: 28px;
    font-weight: 500;
    color: var(--listing-red);
    line-height: 1;
  }

  .association-badge {
    position: absolute;
    left: 368px;
    bottom: 22px;
    width: 124px;
    height: 124px;
    border-radius: 50%;
    background: var(--badge-navy);
  }
</style>
</head>
<body>
<main class="canvas">

  <section class="card card--front" aria-label="Business card front">
    <div class="brand-mark">
      <span class="brand-mark__name">Penhallow<br>Decorating</span>
    </div>
    <p class="front-email">Marla@penhallowdecorating.co.uk</p>
  </section>

  <section class="card card--back" aria-label="Business card back">
    <div class="brand-mark">
      <span class="brand-mark__name">Penhallow<br>Decorating</span>
    </div>

    <div class="contact">
      <h1 class="contact__name">Marla Penhallow</h1>
      <p class="contact__title">Decorator</p>
      <p class="contact__phone">07451 386 902</p>
      <p class="contact__email">Marla@penhallowdecorating.co.uk</p>
      <p class="contact__social">
        <span>@penhallowdecor</span>
        <span class="social-square" aria-hidden="true"></span>
      </p>
    </div>

    <div class="listing">
      <p class="listing__lead">Proud members of</p>
      <p class="listing__name">tradeverify</p>
    </div>

    <div class="association-badge" role="img" aria-label="HFG membership badge"></div>
  </section>

</main>
</body>
</html>
```